Cloud Based Internet Protection Service Business Cards

I would like a professionally designed business card. I already have a logo which I have attached.

The business is an online cloud based internet protection service aimed parents, particularly at non-technical parents and also schools.

The card should be be quite simple in its design, not to full of text and give its information in a clear and concise manner

Target Market(s)

Parents (especially non-technical parents) and also schools

Industry/Entity Type

Internet

Colors

Designer to choose colors to be used in the design.

Requirements
Should not have
• Too much text or be too cluttered. No decorative fonts, just a clear and concise font.

```html
<!DOCTYPE html>
<html lang="en">
<head>
<meta charset="utf-8">
<title>CloudHaven Business Cards</title>
<link href="https://fonts.googleapis.com/css2?family=Open+Sans:wght@400;600&family=Lobster&family=Dancing+Script:wght@400&display=swap" rel="stylesheet">
<style>
  :root {
    --page: #eef1f5;
    --navy-deep: #12328a;
    --navy: #1d47a8;
    --sky: #2f9be0;
    --sky-light: #5fc3f2;
    --cloud-white: #eef6fb;
    --text-white: #ffffff;
    --text-soft: #d9e6fb;
  }
  * { box-sizing: border-box; margin: 0; padding: 0; }
  html, body { width: 1200px; height: 845px; overflow: hidden; }
  body {
    background: var(--page);
    font-family: "Open Sans", Arial, sans-serif;
    display: flex;
    align-items: center;
    justify-content: center;
    gap: 60px;
  }
  .card {
    position: relative;
    width: 525px;
    height: 300px;
    border-radius: 18px;
    overflow: hidden;
    background: radial-gradient(ellipse at 45% 45%, var(--navy) 0%, var(--navy-deep) 100%);
    box-shadow: 0 6px 18px rgba(18, 50, 138, 0.25);
    color: var(--text-white);
  }
  .cloud-art {
    position: absolute;
    background: radial-gradient(ellipse at center, var(--cloud-white) 0%, var(--sky-light) 35%, var(--sky) 70%, rgba(47,155,224,0) 100%);
  }
  .card-front .cloud-art--bottom-left { left: -70px; bottom: -60px; width: 300px; height: 200px; border-radius: 50%; }
  .card-front .cloud-art--top-right { right: -80px; top: -70px; width: 300px; height: 230px; border-radius: 50%; }
  .brand {
    position: absolute;
    left: 50%;
    top: 50%;
    transform: translate(-50%, -50%);
    display: flex;
    align-items: center;
    gap: 14px;
  }
  .brand-dot {
    width: 44px; height: 44px;
    border-radius: 50%;
    background: var(--text-white);
  }
  .brand-name {
    font-weight: 600;
    font-size: 34px;
    letter-spacing: 3px;
    color: var(--text-white);
  }
  .card-back .cloud-art--bottom-right { right: -90px; bottom: -90px; width: 380px; height: 260px; border-radius: 50%; }
  .identity {
    position: absolute;
    left: 40px;
    top: 62px;
  }
  .person-name {
    font-family: "Lobster", Georgia, cursive;
    font-size: 46px;
    line-height: 1;
  }
  .person-role {
    font-family: "Dancing Script", Georgia, cursive;
    font-size: 18px;
    color: var(--text-soft);
    margin-left: 40px;
  }
  .contact {
    position: absolute;
    list-style: none;
    font-size: 14px;
    color: var(--text-soft);
  }
  .contact li { display: flex; align-items: center; gap: 10px; margin-bottom: 10px; }
  .contact svg { width: 13px; height: 13px; fill: var(--text-soft); flex: none; }
  .contact--address { left: 40px; bottom: 40px; }
  .contact--online { right: 36px; top: 30px; }
</style>
</head>
<body>
  <section class="card card-front" aria-label="Business card front">
    <div class="cloud-art cloud-art--bottom-left" role="img" aria-label="Illustrated blue and white clouds"></div>
    <div class="cloud-art cloud-art--top-right" role="img" aria-label="Illustrated blue and white clouds"></div>
    <div class="brand">
      <span class="brand-dot"></span>
      <span class="brand-name">CLOUDHAVEN</span>
    </div>
  </section>

  <section class="card card-back" aria-label="Business card back">
    <div class="cloud-art cloud-art--bottom-right" role="img" aria-label="Illustrated blue and white clouds"></div>
    <ul class="contact contact--online">
      <li><svg viewBox="0 0 16 16"><path d="M1 3h14v10H1z M2 4l6 5 6-5" fill="none" stroke="#d9e6fb" stroke-width="1.5"/></svg>info@example.com</li>
      <li><svg viewBox="0 0 16 16"><circle cx="8" cy="8" r="6.5" fill="none" stroke="#d9e6fb" stroke-width="1.5"/><path d="M1.5 8h13M8 1.5c-3 3.5-3 9.5 0 13M8 1.5c3 3.5 3 9.5 0 13" fill="none" stroke="#d9e6fb" stroke-width="1.2"/></svg>www.example.com</li>
    </ul>
    <div class="identity">
      <p class="person-name">Name</p>
      <p class="person-role">Designation</p>
    </div>
    <ul class="contact contact--address">
      <li><svg viewBox="0 0 16 16"><path d="M8 1a5 5 0 0 0-5 5c0 4 5 9 5 9s5-5 5-9a5 5 0 0 0-5-5zm0 7a2 2 0 1 1 0-4 2 2 0 0 1 0 4z"/></svg>Street, city, state.</li>
      <li><svg viewBox="0 0 16 16"><path d="M4 1l3 3-2 2c1 2 3 4 5 5l2-2 3 3-2 3C7 14 2 9 1 3z"/></svg>123-456-7890</li>
    </ul>
  </section>
</body>
</html>
```